Stationery Design for Tierhaven

We already have a logo a Logo for our outstanding veterinary hospital. Now we are looking for our future letterhead, business cards and envelopes. We would like to see a design using the color from our logo. Additional color should be limited to grey or a rusty brown. The font should be easy and clearly readable and must be easily available on all computers (to install it in our Management software). The finial design should communicate competence in veterinary medicine, and empathy.

To meet the European regulation (DIN5008) there are a couple mandatory legal informations one the letterhead. We also enclosed a template of exact measurement, which need to be respected according to DIN5008.

Mandatory legal information are (best placed in the footer):
"Tierhaven GmbH & Co KG, Ostrowgasse 417C, 1230 Wien,
Handelsgericht Wien, FN 924615k, GF: Dr. Lukas Brandl
ATU 3148926"
Additional informations needed:
"Tel: +43 1 5849163, Fax: +43 1 5849164, info@tierhaven-example.at, www. tierhaven-example.at"
bank account informations should be included as well. These are:
"Sparkasse Obergruntal, IBAN: AT 58 1111 2222 3333 4444, BIC: SPKTAT4K817"

The Logo should be in the upper right corner. Below that we need a space for informations regarding the responsible veterinarians. There will be 3-5 Names, each of it consisting of 2 lines (see example below). The Names should be highlighted (larger font) compared to the qualifications in the second line.
Tierärztliche Leitung:
Dr. Lukas Brandl
Diplomate ECVS

The contest was startet on the 2nd of may and the deadline was a day later? Why was that so fast? Did I do something wrong? BR

Target Market(s)

dog and cat owner in Austria as welle as referring veterinarians in Austria

Industry/Entity Type

Veterinary

Contact Information for Business Card

One side: Logo
other side:
Dr. Lukas Brandl
Diplomate ECVS
EBVS Specialist of Small Animal Surgery

Tierhaven GmbH&Co KG
Ostrowgasse 417C
1230 Wien

Tel: +43 1 6210000 DW 102
Fax: +43 1 6210000 DW 999
email: lukas.brandl@tierhaven-example.at

Font styles to use
Serif
Sans Serif

Requirements
Must have
• The logo should be given in the upper right. Most of the legal informations should be given in the footer. The upper left Area should be clear, since the recipient address will be placed there.
Colors should be limited to golden, blue and greyscale (two different gereysacales at most).

```html
<!DOCTYPE html>
<html lang="de">
<head>
<meta charset="utf-8">
<title>Tierhaven – Geschäftsausstattung</title>
<link rel="stylesheet" href="https://fonts.googleapis.com/css2?family=Open+Sans:wght@400;600;700&family=Lato:wght@300;400;700&family=Pinyon+Script&display=swap">
<style>
  :root{
    --navy:#1b2550;
    --gold:#c9a02a;
    --grey:#6e6e70;
    --paper:#f4f4f4;
    --faint:#e3e3e5;
    --stage:#e6e6e6;
  }
  *{margin:0;padding:0;box-sizing:border-box}
  html,body{width:1200px;height:1019px;overflow:hidden;background:var(--stage)}
  body{position:relative;font-family:"Open Sans",Arial,sans-serif;color:var(--navy)}
  .sheet{position:absolute;background:var(--paper);overflow:hidden}
  .abs{position:absolute}
  .mark-circle{position:absolute;border-radius:50%;border:2px solid var(--gold);background:var(--navy)}
  .brand{font-family:"Open Sans",Arial,sans-serif;font-weight:700;color:var(--navy);letter-spacing:-.02em;line-height:1;white-space:nowrap}
  .tagline{font-weight:600;color:var(--gold);white-space:nowrap;line-height:1}
  .deco{position:absolute;border-radius:50%;border:6px solid var(--faint);background:rgba(0,0,0,.015)}

  /* letterhead */
  .letterhead{left:157px;top:151px;width:436px;height:617px}
  .letterhead .mark-circle{left:341px;top:21px;width:44px;height:44px}
  .letterhead .brand{right:31px;top:70px;font-size:16px}
  .letterhead .tagline{right:31px;top:85px;font-size:7px}
  .lead-title{right:31px;top:98px;font-size:8.5px;color:var(--grey);letter-spacing:.02em}
  .vets{top:113px;font-size:7.3px;line-height:8.9px;text-align:right}
  .vets .name{color:var(--navy)}
  .vets .qual{color:var(--grey)}
  .vets-left{right:107px}
  .vets-right{right:31px}
  .vets-divider{left:336px;top:114px;width:1px;height:34px;background:var(--gold)}
  .letter{left:46px;width:344px;font-family:Lato,Arial,sans-serif;font-weight:300;font-size:7.1px;line-height:10.3px;color:#333}
  .letter p{text-align:justify;margin-bottom:10.3px}
  .letter strong{font-weight:700}
  .signature{left:50px;top:500px;font-family:"Pinyon Script",cursive;font-size:14px;color:#222}
  .foot{top:563px;font-size:7px;line-height:8.9px;white-space:nowrap}
  .foot-legal{left:31px}
  .foot-legal .sub{color:var(--grey)}
  .foot-contact{left:184px;color:var(--grey)}
  .foot-contact span{display:flex;align-items:center;gap:3px}
  .foot-bank{right:31px;text-align:right;color:var(--grey)}
  .foot-divider{top:565px;width:1px;height:33px;background:#b5b5b5}
  .icon{width:6px;height:6px;fill:var(--navy)}
  .band{position:absolute;left:0;bottom:0;width:100%;height:6px}

  /* business cards */
  .card-front{left:625px;top:139px;width:227px;height:130px}
  .card-front .mark-circle{left:161px;top:12px;width:33px;height:33px;border-width:1.5px}
  .card-front .brand{right:17px;top:48px;font-size:11px}
  .card-front .tagline{right:17px;top:60px;font-size:5px}
  .holder{left:17px;top:63px;font-size:7px;font-weight:700;white-space:nowrap}
  .holder-qual{left:17px;top:72px;font-size:5px;color:var(--gold)}
  .card-rule{left:17px;top:82px;width:193px;height:1px;background:#c9c9c9}
  .card-contact{left:17px;top:88px;font-size:5px;line-height:6.5px;color:var(--grey)}
  .card-contact span{display:flex;align-items:center;gap:2px}
  .card-contact .icon{width:4px;height:4px}
  .card-address{right:17px;top:94px;font-size:5px;line-height:6.5px;color:var(--grey);text-align:right;white-space:nowrap}
  .card-front .band{height:5px}

  .card-back{left:897px;top:139px;width:227px;height:130px;background:var(--navy)}
  .card-back .deco{left:110px;top:0;width:130px;height:130px;border-color:rgba(255,255,255,.06);background:rgba(255,255,255,.04)}
  .card-back .brand{left:19px;top:86px;font-size:17px;color:#fff}
  .card-back .tagline{left:19px;top:106px;font-size:7.5px}

  /* envelopes */
  .envelope-front{left:624px;top:297px;width:501px;height:217px}
  .envelope-front .deco,.envelope-back .deco{left:315px;top:6px;width:202px;height:202px}
  .envelope-front .mark-circle{left:59px;top:25px;width:42px;height:42px}
  .envelope-front .brand{left:80px;top:70px;font-size:15px;transform:translateX(-50%)}
  .envelope-front .tagline{left:80px;top:85px;font-size:7px;transform:translateX(-50%)}
  .env-divider{left:127px;top:68px;width:1px;height:23px;background:#b5b5b5}
  .env-address{left:136px;top:66px;font-size:7.5px;line-height:9px;color:var(--grey);white-space:nowrap}
  .env-window{left:40px;top:137px;width:145px;height:50px;border-radius:5px;border:1px solid #c6c6c6;background:linear-gradient(110deg,#d4d4d4,#eeeeee 55%,#cfcfcf)}
  .envelope-front .band{height:8px}

  .envelope-back{left:624px;top:551px;width:501px;height:217px}
  .env-flap{left:0;top:0;width:33px;height:217px}
</style>
</head>
<body>

<!-- Letterhead -->
<section class="sheet letterhead" aria-label="Briefbogen">
  <div class="deco" style="left:108px;top:250px;width:220px;height:220px"></div>
  <div class="mark-circle"></div>
  <div class="abs brand">Tierhaven</div>
  <div class="abs tagline">Fachklinik für Kleintiere</div>
  <div class="abs lead-title">Tierärztliche Leitung</div>
  <div class="abs vets vets-left">
    <div class="name">Dr. Anna Steiner</div><div class="qual">Diplomate EVCS</div>
    <div class="name">Dr. Felix Haider</div><div class="qual">EBVS Specialist</div>
  </div>
  <div class="abs vets-divider"></div>
  <div class="abs vets vets-right">
    <div class="name">Dr. Lukas Brandl</div><div class="qual">Diplomate EVCS</div>
    <div class="name">Dr. M. Kogler</div><div class="qual">EBVS Specialist</div>
  </div>

  <div class="abs letter" style="top:170px">01 January 2050</div>
  <div class="abs letter" style="top:191px"><strong>Company (Pvt) Ltd.</strong><br>PO Box 4821 Lindenweg St<br>Sample City Country 4821</div>
  <div class="abs letter" style="top:242px">Dear Paul Redlinger,</div>
  <div class="abs letter" style="top:263px">
    <p>Lorem ipsum dolor sit amet, consectetuer adipiscing elit, sed diam nonummy nibh euismod tincidunt ut laoreet dolore magna aliquam erat volutpat. Ut wisi enim ad minim veniam, quis nostrud exerci tation ullamcorper suscipit lobortis nisl ut aliquip ex ea commodo consequat. Duis dolore te feugait nulla facilisi. Nam liber tempor cum soluta nobis eleifend option congue nihil imperdiet doming id quod mazim placerat facer possim assum. Lorem ipsum dolor sit amet, consectetuer adipiscing elit, sed diam nonummy nibh euismod tincidunt ut laoreet dolore magna aliquam erat volutpat. Ut wisi enim ad minim veniam, quis nostrud exerci tation ullamcorper suscipit lobortis nisl ut aliquip ex ea commodo consequat.</p>
    <p>Consectetuer adipiscing elit, sed diam nonummy nibh euismod tincidunt ut laoreet dolore magna aliquam erat volutpat. Ut wisi enim ad minim veniam, quis nostrud exerci tation ullamcorper suscipit lobortis nisl ut aliquip ex ea commodo consequat. Consectetuer adipiscing elit, sed diam nonummy nibh euismod tincidunt ut laoreet dolore magna aliquam erat volutpat. Ut wisi enim ad minim veniam, quis nostrud exerci tation ullamcorper suscipit lobortis nisl ut aliquip ex ea commodo consequat.</p>
    <p>Consectetuer adipiscing elit, sed diam nonummy nibh euismod tincidunt ut laoreet dolore magna aliquam erat volutpat. Ut wisi enim ad minim veniam, quis nostrud exerci tation ullamcorper suscipit lobortis nisl ut aliquip ex ea commodo consequat. Consectetuer adipiscing elit, sed diam nonummy nibh euismod tincidunt ut laoreet dolore magna aliquam erat volutpat. Ut wisi enim ad minim veniam, quis nostrud exerci tation ullamcorper suscipit lobortis nisl ut aliquip ex ea commodo consequat.</p>
  </div>
  <div class="abs letter" style="top:489px">Sincerely Yours</div>
  <div class="abs signature">Thomas Georg Wallner</div>

  <div class="abs foot foot-legal">
    <div>Tierhaven GmbH &amp; Co KG</div>
    <div>Ostrowgasse 417C, 1230 Wien</div>
    <div class="sub">Handelsgericht Wien, FN 924615k</div>
    <div class="sub">GF: Dr. Lukas Brandl, ATU 3148926</div>
  </div>
  <div class="abs foot-divider" style="left:169px"></div>
  <div class="abs foot foot-contact">
    <span><svg class="icon" viewBox="0 0 10 10"><path d="M2 0.5 3.8 2.8 2.9 4a6 6 0 0 0 3.1 3.1l1.2-.9L9.5 8 8.4 9.5C4.5 9.5.5 5.5.5 1.6z"/></svg>+43 (1) 584 9163</span>
    <span><svg class="icon" viewBox="0 0 10 10"><path d="M2.5 0h5v3h-5zM0 3.5h10v4H8V10H2V7.5H0zM3 6.5v2.5h4V6.5z"/></svg>+43 (1) 584 9164</span>
    <span><svg class="icon" viewBox="0 0 10 10"><path d="M0 2h10v6H0zm.8.6L5 5.5 9.2 2.6z" fill-rule="evenodd"/></svg>info@tierhaven-example.at</span>
    <span><svg class="icon" viewBox="0 0 10 10"><circle cx="5" cy="5" r="4.3" fill="none" stroke="#1b2550" stroke-width="1"/><path d="M.7 5h8.6M5 .7c-2.4 2.6-2.4 6 0 8.6M5 .7c2.4 2.6 2.4 6 0 8.6" fill="none" stroke="#1b2550" stroke-width=".8"/></svg>www.tierhaven-example.at</span>
  </div>
  <div class="abs foot-divider" style="left:277px"></div>
  <div class="abs foot foot-bank">
    <div>Sparkasse Obergruntal</div>
    <div>IBAN: AT 58 1111 2222 3333 4444</div>
    <div>BIC: SPKTAT4K817</div>
  </div>
  <svg class="band" viewBox="0 0 436 6" preserveAspectRatio="none"><polygon points="0,0 222,0 218,6 0,6" fill="#1b2550"/><polygon points="222,0 436,0 436,6 218,6" fill="#c9a02a"/></svg>
</section>

<!-- Business card, front -->
<section class="sheet card-front" aria-label="Visitenkarte Vorderseite">
  <div class="mark-circle"></div>
  <div class="abs brand">Tierhaven</div>
  <div class="abs tagline">Fachklinik für Kleintiere</div>
  <div class="abs holder">Dr. Lukas Brandl</div>
  <div class="abs holder-qual">Diplomate ECVS</div>
  <div class="abs card-rule"></div>
  <div class="abs card-contact">
    <span><svg class="icon" viewBox="0 0 10 10"><path d="M2 0.5 3.8 2.8 2.9 4a6 6 0 0 0 3.1 3.1l1.2-.9L9.5 8 8.4 9.5C4.5 9.5.5 5.5.5 1.6z"/></svg>+43 (1) 584 9163</span>
    <span><svg class="icon" viewBox="0 0 10 10"><path d="M2.5 0h5v3h-5zM0 3.5h10v4H8V10H2V7.5H0zM3 6.5v2.5h4V6.5z"/></svg>+43 (1) 584 9164</span>
    <span><svg class="icon" viewBox="0 0 10 10"><path d="M0 2h10v6H0zm.8.6L5 5.5 9.2 2.6z" fill-rule="evenodd"/></svg>info@tierhaven-example.at</span>
    <span><svg class="icon" viewBox="0 0 10 10"><circle cx="5" cy="5" r="4.3" fill="none" stroke="#1b2550" stroke-width="1"/><path d="M.7 5h8.6" stroke="#1b2550"/></svg>www.tierhaven-example.at</span>
  </div>
  <div class="abs card-address">
    <div>Tierhaven GmbH &amp; Co KG</div>
    <div>Ostrowgasse 417C, 1230 Wien</div>
    <div>Handelsgericht Wien, FN 924615k</div>
  </div>
  <svg class="band" viewBox="0 0 227 5" preserveAspectRatio="none"><polygon points="0,0 116,0 113,5 0,5" fill="#1b2550"/><polygon points="116,0 227,0 227,5 113,5" fill="#c9a02a"/></svg>
</section>

<!-- Business card, back -->
<section class="sheet card-back" aria-label="Visitenkarte Rückseite">
  <div class="deco"></div>
  <div class="abs brand">Tierhaven</div>
  <div class="abs tagline">Fachklinik für Kleintiere</div>
</section>

<!-- Window envelope -->
<section class="sheet envelope-front" aria-label="Fensterkuvert">
  <div class="deco"></div>
  <div class="mark-circle"></div>
  <div class="abs brand">Tierhaven</div>
  <div class="abs tagline">Fachklinik für Kleintiere</div>
  <div class="abs env-divider"></div>
  <div class="abs env-address">
    <div>Tierhaven GmbH &amp; Co KG</div>
    <div>Ostrowgasse 417C, 1230 Wien</div>
    <div>Handelsgericht Wien, FN 924615k</div>
  </div>
  <div class="abs env-window"></div>
  <svg class="band" viewBox="0 0 501 8" preserveAspectRatio="none"><polygon points="0,0 49,0 44,8 0,8" fill="#c9a02a"/><polygon points="49,0 501,0 501,8 44,8" fill="#1b2550"/></svg>
</section>

<!-- Envelope, back -->
<section class="sheet envelope-back" aria-label="Kuvert Rückseite">
  <div class="deco"></div>
  <svg class="abs env-flap" viewBox="0 0 33 217" preserveAspectRatio="none"><path d="M0,0 L28,8 Q33,10 33,16 L33,201 Q33,207 28,209 L0,217 Z" fill="#171d4c"/></svg>
</section>

</body>
</html>
```